Design Website Templates for Photographers for Lumora Inc. (trywendle.com)

Lumora Inc. is a generative website company for wedding photographers.
We are seeking new photography website design inspirations for the next template to be offered on our platform. The catch is you must use the same data for your designs. You also must use all of the data somewhere in the design. You cannot add new content besides the data available. If you wish to add any elements It will be hardcoded and must be universally fitting for many different photographers. We recommend not using any hardcoded test.
Don't be afraid to be creative! Although the most important element of a photographers website is the photos, we are looking for unique and out-of-the-box designs for the actual site as well.
Here is the User generated data available to you:
- 4 Hero Images Landscape, 4 Hero Images Portrait
- Tagline “destination photographer based in Maui, Hawaii”
- “About Photo” of the photographer
- “About” Biography Text
- The design can use up to 3 colors + background color and 2 fonts
- 9 Gallery images
- 3 Packages/services that include landscape/portrait images, a price, a title and text
- Testimonials made up of an image, text and text for the name of testimonial giver
See some examples of our current website designs attached. You can use any of the data you see in the designs.
Updates
We are looking for designs that are less feminine and are more neutral in color and fonts. Currently our templates are more oriented towards feminine photographers. We want to have designs that speak to diverse audiences. We thank everyone for submitting and are reviewing the designs.
Number of Pages Required
1 page
Look and feel
Each slider illustrates characteristics of the customer's brand and the style your logo design should communicate.

```html
<!DOCTYPE html>
<html lang="en">
<head>
<meta charset="utf-8">
<title>Lumora — Destination Photographer</title>
<link href="https://fonts.googleapis.com/css2?family=Poppins:wght@400;500;600;700&family=Tinos&display=swap" rel="stylesheet">
<style>
:root{
  --gold:#efb84a;
  --slate:#58585b;
  --bronze:#9a7d4e;
  --ink:#111111;
  --white:#ffffff;
  --dark:#1e1e1e;
}
*{margin:0;padding:0;box-sizing:border-box}
html,body{width:1200px;height:3836px;overflow:hidden}
body{position:relative;font-family:"Poppins",sans-serif;background:var(--slate);color:var(--white)}
.abs{position:absolute}
.photo{position:absolute}

/* header */
.site-header{left:0;top:0;width:1200px;height:58px;background:var(--gold)}
.brand{left:112px;top:16px;font-size:22px;font-weight:500;letter-spacing:3px;color:#3a3a3a;display:flex;align-items:center;gap:8px;line-height:26px}
.brand-dot{width:9px;height:9px;border-radius:50%;background:#3a3a3a}
.main-nav{left:295px;top:24px;display:flex;gap:31px;font-size:15px;line-height:18px;color:var(--white);text-transform:uppercase;letter-spacing:.3px}
.search-icon{left:1117px;top:20px}

/* hero */
.hero{left:0;top:58px;width:1200px;height:493px;
  background:
    radial-gradient(ellipse 230px 300px at 880px 300px,rgba(36,52,140,.85) 0%,rgba(36,52,140,.55) 45%,rgba(36,52,140,0) 100%),
    radial-gradient(ellipse 160px 220px at 760px 470px,rgba(170,150,120,.55) 0%,rgba(170,150,120,0) 100%),
    linear-gradient(180deg,#c2c8d0 0%,#98a3b0 40%,#5a6476 66%,#27304a 84%,#141a2a 100%)}
.hero-title{left:100px;top:220px;width:570px;text-align:center;font-size:36px;font-weight:700;line-height:52px;color:#1f1f22;letter-spacing:.5px}
.btn{background:var(--gold);color:var(--white);font-weight:600;text-transform:uppercase;display:flex;align-items:center;justify-content:center}
.hero-book{left:235px;top:351px;width:230px;height:56px;font-size:21px}
.slider-arrow{position:absolute}

/* sections */
.section-title{font-size:31px;line-height:40px;font-weight:700;text-transform:uppercase;letter-spacing:.4px}
.copy{font-size:16px;line-height:25.7px;color:#f0f0f0}
.copy p+p{margin-top:9px}
.read-more{height:45px;font-size:18px;gap:8px}

.about-title{left:116px;top:643px}
.about-copy{left:113px;top:699px;width:520px}
.about-btn{left:112px;top:926px;width:171px}
.about-frame{left:689px;top:661px;width:398px;height:307px;background:#000;box-shadow:4px 4px 8px rgba(0,0,0,.35)}
.about-photo{left:707px;top:695px;width:361px;height:243px;border:4px solid var(--white);
  background:radial-gradient(circle at 36% 52%,#d6dbe2 0%,#7b7f86 14%,#1b1b1d 30%,#2b2b2d 44%,#0e0e0f 52%,rgba(14,14,15,0) 62%),linear-gradient(90deg,#3a3a3c 0%,#d8d6d4 60%,#ecebea 100%)}

.bio-photo{left:112px;top:1090px;width:399px;height:307px;box-shadow:4px 4px 8px rgba(0,0,0,.35);
  background:radial-gradient(ellipse 110px 150px at 200px 190px,#b39a78 0%,rgba(179,154,120,0) 100%),linear-gradient(135deg,#55636a 0%,#6e7a7d 45%,#3a4246 100%)}
.bio-title{left:625px;top:1077px}
.bio-copy{left:627px;top:1126px;width:455px}
.bio-btn{left:631px;top:1359px;width:172px}

.gallery-title{left:0;top:1509px;width:1200px;text-align:center}
.gallery-tile{width:320px;height:262px;box-shadow:3px 3px 6px rgba(0,0,0,.35)}

.packages-title{left:0;top:2513px;width:1200px;text-align:center}
.package-card{width:307px;height:341px;background:var(--white);color:var(--dark)}
.package-photo{position:absolute;left:0;top:0;width:307px;height:247px}
.package-name{position:absolute;left:14px;top:259px;font-size:21px;line-height:26px;font-weight:700;text-transform:uppercase}
.package-price{position:absolute;left:20px;top:292px;font-size:25px;line-height:32px;font-weight:700}
.package-arrow{position:absolute;right:22px;top:306px}

/* testimonials */
.testimonials{left:0;top:3030px;width:1200px;height:480px;background:var(--bronze)}
.testimonials-title{left:0;top:3057px;width:1200px;text-align:center}
.review-card{width:395px;height:290px;top:3167px;background:var(--white);border:4px solid var(--gold);border-radius:8px;color:#2a2a2a}
.reviewer{position:absolute;left:32px;top:24px;font-size:18px;line-height:24px;font-weight:600}
.stars{position:absolute;right:36px;top:19px;font-size:16px;line-height:20px;letter-spacing:1px;color:#1a1a1a}
.review-text{position:absolute;left:24px;top:104px;width:350px;font-size:16px;line-height:27.5px;color:#333}
.avatar{width:124px;height:124px;top:3111px;border-radius:50%;border:4px solid var(--gold);
  background:radial-gradient(ellipse 38px 46px at 50% 42%,#8a6e5e 0%,rgba(138,110,94,0) 100%),linear-gradient(180deg,#b9b9b9 0%,#8c8c8c 100%)}

/* footer */
.site-footer{left:0;top:3510px;width:1200px;height:326px;background:var(--ink)}
.footer-brand{left:0;top:3560px;width:1200px;justify-content:center;display:flex;align-items:center;gap:14px;font-size:62px;line-height:72px;font-weight:400;letter-spacing:8px;color:#3c3c3c}
.footer-brand-dot{width:24px;height:24px;border-radius:50%;background:var(--gold)}
.footer-nav{left:0;top:3673px;width:1200px;display:flex;justify-content:center;gap:35px;font-size:16px;line-height:20px;font-weight:600;letter-spacing:1.6px;text-transform:uppercase}
.social{left:0;top:3732px;width:1200px;display:flex;justify-content:center;gap:10px}
.social-link{width:30px;height:30px;border-radius:50%;background:var(--white);display:flex;align-items:center;justify-content:center}
.social-link::after{content:"";width:14px;height:14px;border-radius:50%;background:var(--ink)}
.footer-rule{left:0;top:3792px;width:1200px;height:1px;background:#555}
.copyright{left:0;top:3804px;width:1200px;text-align:center;font-family:"Tinos",serif;font-size:15px;line-height:18px;color:#ddd}
</style>
</head>
<body>

<header class="abs site-header"></header>
<div class="abs brand"><span>LUMORA</span><span class="brand-dot"></span></div>
<nav class="abs main-nav"><span>Home</span><span>About</span><span>Photography</span><span>About Biography</span><span>Gallery</span><span>Testimonials</span><span>Pricing</span></nav>
<svg class="abs search-icon" width="28" height="28" viewBox="0 0 28 28"><circle cx="11" cy="11" r="8" fill="none" stroke="#fff" stroke-width="3.5"/><line x1="17" y1="17" x2="25" y2="25" stroke="#fff" stroke-width="4" stroke-linecap="round"/></svg>

<section class="abs hero" role="img" aria-label="Couple embracing on a mountain lookout at dusk"></section>
<h1 class="abs hero-title">DESTINATION PHOTOGRAPHER<br>BASED IN MAUI, HAWAII</h1>
<div class="abs btn hero-book">Book Now</div>
<svg class="slider-arrow" style="left:23px;top:276px" width="46" height="46" viewBox="0 0 46 46"><circle cx="23" cy="23" r="21" fill="none" stroke="#111" stroke-width="2.5"/><path d="M33 23H13M20 16l-7 7 7 7" fill="none" stroke="#111" stroke-width="2.5"/></svg>
<svg class="slider-arrow" style="left:1127px;top:270px" width="46" height="46" viewBox="0 0 46 46"><circle cx="23" cy="23" r="21" fill="none" stroke="#111" stroke-width="2.5"/><path d="M13 23h20M26 16l7 7-7 7" fill="none" stroke="#111" stroke-width="2.5"/></svg>

<h2 class="abs section-title about-title">About Photography</h2>
<div class="abs copy about-copy">
  <p>Lorem ipsum dolor sit amet, consectetur adipiscing elit, sed do eiusmod tempor incididunt ut labore et dolore magna aliqua. Ut enim ad minim veniam, quis nostrud exercitation ullamco laboris nisi ut aliquip ex ea commodo consequat</p>
  <p>Duis aute irure dolor in reprehenderit in voluptate velit esse cillum dolore eu fugiat nulla pariatur. Excepteur sint occaecat cupidatat non proident, sunt in culpa qui officia deserunt mollit anim id est laborum."</p>
</div>
<div class="abs btn read-more about-btn">Read More <svg width="24" height="10" viewBox="0 0 24 10"><path d="M0 5h22M17 1l5 4-5 4" fill="none" stroke="#fff" stroke-width="2"/></svg></div>
<div class="abs about-frame"></div>
<div class="photo about-photo" role="img" aria-label="Close-up of a camera lens"></div>

<div class="photo bio-photo" role="img" aria-label="Photographer holding a camera to his eye"></div>
<h2 class="abs section-title bio-title">My Biography</h2>
<div class="abs copy bio-copy">
  <p>Lorem ipsum dolor sit amet, consectetur adipiscing elit, sed do eiusmod tempor incididunt ut labore et dolore magna aliqua. Ut enim ad minim veniam, quis nostrud exercitation ullamco laboris nisi ut aliquip ex ea</p>
  <p>Duis aute irure dolor in reprehenderit in voluptate velit esse cillum dolore eu fugiat nulla pariatur. Excepteur sint occaecat cupidatat non proident, sunt in culpa qui officia deserunt mollit anim id est laborum."</p>
</div>
<div class="abs btn read-more bio-btn">Read More <svg width="24" height="10" viewBox="0 0 24 10"><path d="M0 5h22M17 1l5 4-5 4" fill="none" stroke="#fff" stroke-width="2"/></svg></div>

<h2 class="abs section-title gallery-title">Gallery</h2>
<div class="photo gallery-tile" style="left:104px;top:1587px;background:radial-gradient(ellipse 70px 110px at 185px 170px,rgba(230,40,170,.8) 0%,rgba(230,40,170,0) 100%),linear-gradient(180deg,#a89b90 0%,#8d8a8c 52%,#3d6d94 62%,#2f5c80 100%)" role="img" aria-label="Couple by the sea, bride in a pink gown"></div>
<div class="photo gallery-tile" style="left:444px;top:1590px;background:radial-gradient(ellipse 130px 80px at 230px 110px,rgba(32,60,200,.9) 0%,rgba(32,60,200,0) 100%),linear-gradient(180deg,#9ec3de 0%,#c9d8e2 40%,#5f8fa3 100%)" role="img" aria-label="Couple with a flowing blue gown"></div>
<div class="photo gallery-tile" style="left:780px;top:1587px;background:radial-gradient(ellipse 120px 110px at 110px 120px,rgba(200,30,55,.9) 0%,rgba(200,30,55,0) 100%),linear-gradient(135deg,#b56a74 0%,#c4a6a6 55%,#d6c3c2 100%)" role="img" aria-label="Couple among red petals"></div>
<div class="photo gallery-tile" style="left:104px;top:1867px;background:linear-gradient(135deg,#7a4a3a 0%,#6b4334 55%,#3a2c26 100%)" role="img" aria-label="Couple in formal wear against a brown wall"></div>
<div class="photo gallery-tile" style="left:444px;top:1867px;background:linear-gradient(180deg,#3e4658 0%,#6f6a72 40%,#b07a62 56%,#2a2c34 70%,#1c1c22 100%)" role="img" aria-label="Couple at dusk by still water"></div>
<div class="photo gallery-tile" style="left:780px;top:1867px;background:linear-gradient(180deg,#e6b58c 0%,#e8c0a0 45%,#8ea3ad 62%,#c9b9a6 100%)" role="img" aria-label="Couple on a beach at sunset"></div>
<div class="photo gallery-tile" style="left:104px;top:2147px;background:radial-gradient(ellipse 110px 60px at 120px 220px,rgba(220,40,40,.85) 0%,rgba(220,40,40,0) 100%),linear-gradient(180deg,#8ad6e2 0%,#2fb0b6 45%,#6e5e52 75%,#4e4540 100%)" role="img" aria-label="Couple on rocks with a red gown by turquoise sea"></div>
<div class="photo gallery-tile" style="left:444px;top:2149px;background:radial-gradient(ellipse 90px 90px at 170px 180px,rgba(70,50,130,.85) 0%,rgba(70,50,130,0) 100%),linear-gradient(135deg,#d7a561 0%,#b5864a 60%,#8a6234 100%)" role="img" aria-label="Couple dancing in warm golden light"></div>
<div class="photo gallery-tile" style="left:780px;top:2147px;background:radial-gradient(ellipse 60px 110px at 150px 170px,rgba(130,190,180,.8) 0%,rgba(130,190,180,0) 100%),linear-gradient(90deg,#8a7262 0%,#c9b39f 50%,#7a6a5c 100%)" role="img" aria-label="Couple in a columned corridor"></div>

<h2 class="abs section-title packages-title">Packages</h2>
<div class="abs package-card" style="left:116px;top:2575px">
  <div class="package-photo" style="background:radial-gradient(ellipse 110px 110px at 120px 130px,#f6f4f2 0%,rgba(246,244,242,0) 100%),linear-gradient(135deg,#c9c3bd 0%,#9a958f 50%,#2f3036 100%)" role="img" aria-label="Bride and groom with a bouquet"></div>
  <div class="package-name">Wedding Collection</div>
  <div class="package-price">$500</div>
  <svg class="package-arrow" width="38" height="12" viewBox="0 0 38 12"><path d="M0 6h35M30 1l6 5-6 5" fill="none" stroke="#111" stroke-width="2"/></svg>
</div>
<div class="abs package-card" style="left:445px;top:2575px">
  <div class="package-photo" style="background:linear-gradient(180deg,#d7a486 0%,#b48a76 40%,#6e6068 62%,#3a3534 100%)" role="img" aria-label="Couple walking along a shore at sunset"></div>
  <div class="package-name">Wedding Collection</div>
  <div class="package-price">$500</div>
  <svg class="package-arrow" width="38" height="12" viewBox="0 0 38 12"><path d="M0 6h35M30 1l6 5-6 5" fill="none" stroke="#111" stroke-width="2"/></svg>
</div>
<div class="abs package-card" style="left:776px;top:2575px">
  <div class="package-photo" style="background:radial-gradient(ellipse 80px 40px at 170px 165px,rgba(220,220,230,.85) 0%,rgba(220,220,230,0) 100%),linear-gradient(180deg,#c3ccce 0%,#b9bfbe 45%,#a38866 62%,#6e5a40 100%)" role="img" aria-label="Bride twirling in a field"></div>
  <div class="package-name">Wedding Collection</div>
  <div class="package-price">$500</div>
  <svg class="package-arrow" width="38" height="12" viewBox="0 0 38 12"><path d="M0 6h35M30 1l6 5-6 5" fill="none" stroke="#111" stroke-width="2"/></svg>
</div>

<section class="abs testimonials"></section>
<h2 class="abs section-title testimonials-title">Testimonials</h2>
<div class="abs review-card" style="left:192px">
  <div class="reviewer">Ajsefi</div>
  <div class="stars">★★★★★</div>
  <p class="review-text">Lorem ipsum dolor sit amet, consectetur adipiscing elit, sed do eiusmod tempor incididunt ut labore et dolore magna aliqua. Ut enim ad minim veniam, quis nostrud exercitation ullamco laboris nisi ut aliquip ex ea commodo consequat.</p>
</div>
<div class="abs avatar" style="left:328px" role="img" aria-label="Portrait of the reviewer"></div>
<div class="abs review-card" style="left:629px">
  <div class="reviewer">Ajsefi</div>
  <div class="stars">★★★★★</div>
  <p class="review-text">Lorem ipsum dolor sit amet, consectetur adipiscing elit, sed do eiusmod tempor incididunt ut labore et dolore magna aliqua. Ut enim ad minim veniam, quis nostrud exercitation ullamco laboris nisi ut aliquip ex ea commodo consequat.</p>
</div>
<div class="abs avatar" style="left:767px" role="img" aria-label="Portrait of the reviewer"></div>
<svg class="slider-arrow" style="left:18px;top:3279px" width="46" height="46" viewBox="0 0 46 46"><circle cx="23" cy="23" r="21" fill="none" stroke="#111" stroke-width="2.5"/><path d="M33 23H13M20 16l-7 7 7 7" fill="none" stroke="#111" stroke-width="2.5"/></svg>
<svg class="slider-arrow" style="left:1121px;top:3270px" width="46" height="46" viewBox="0 0 46 46"><circle cx="23" cy="23" r="21" fill="none" stroke="#111" stroke-width="2.5"/><path d="M13 23h20M26 16l7 7-7 7" fill="none" stroke="#111" stroke-width="2.5"/></svg>

<footer class="abs site-footer"></footer>
<div class="abs footer-brand"><span>LUMORA</span><span class="footer-brand-dot"></span></div>
<nav class="abs footer-nav"><span>Home</span><span>About</span><span>Photography</span><span>About Biography</span><span>Gallery</span><span>Testimonials</span><span>Pricing</span></nav>
<div class="abs social" aria-label="Social links"><span class="social-link"></span><span class="social-link"></span><span class="social-link"></span><span class="social-link"></span></div>
<div class="abs footer-rule"></div>
<div class="abs copyright">© 2023 LUMORA.All Rights Reserved</div>

</body>
</html>
```